Bref créative |
Harbourlea Dental Clinic | ||
business cards, letterhead and envelopes design | ||
Use same font as used in my logo | ||
Cutting-Edge Corporate Traditional Modern Professional Simple Bright & Fun-filled |
Dr. Kelsi Tomberg Ravinder | ||
Corrow Arcade - Shop 4.3C, 27 Fenwick Lane, Meadowbank, NSW 2114 |
kelsi@HarbourleaDentalClinic.com.au | ||
www.HarbourleaDentalClinic.com.au | ||
For Business Cards Please include: After-hours Emergency Service: Phone: 02 5173 6648 Mobile: 04 7825 1943 For Envelops Please include: Logo If not delivered please return to Corrow Arcade - Shop 4.3C, 27 Fenwick Lane, Meadowbank, NSW 2114 |
Appointment: For - Date - Time - If you are unable to keep your appointment, please contact us as soon as possible. |

```html
<!DOCTYPE html>
<html lang="en">
<head>
<meta charset="utf-8">
<title>Harbourlea Dental Clinic – Stationery</title>
<link href="https://fonts.googleapis.com/css2?family=Exo+2:wght@400;700;800&family=Open+Sans:wght@400;600&display=swap" rel="stylesheet">
<style>
:root{
  --bg:#e9ebee;
  --paper:#ffffff;
  --blue:#1b9ad6;
  --navy:#0e3a73;
  --ink:#4a5563;
  --rule:#b9c3cc;
}
*{box-sizing:border-box;margin:0;padding:0}
html,body{width:1200px;height:871px;overflow:hidden;background:var(--bg)}
body{position:relative;font-family:"Open Sans",sans-serif;color:var(--ink)}
.sheet{position:absolute;background:var(--paper);box-shadow:0 1px 3px rgba(0,0,0,.18)}

.brand{font-family:"Exo 2",sans-serif;display:flex;align-items:flex-start;gap:7px}
.brand-dot{flex:none;border-radius:50%;background:var(--blue)}
.brand-name{font-weight:800;color:var(--blue);text-transform:uppercase;line-height:1;letter-spacing:.4px;white-space:nowrap}
.brand-tag{font-family:"Exo 2",sans-serif;font-weight:700;color:var(--navy);line-height:1.2;white-space:nowrap}

/* Letterhead */
.letterhead{left:115px;top:108px;width:394px;height:684px}
.letterhead .brand{position:absolute;left:24px;top:30px}
.letterhead .brand-dot{width:20px;height:20px}
.letterhead .brand-name{font-size:14px}
.letterhead .brand-tag{font-size:8px;margin-top:3px}
.lh-address{position:absolute;right:22px;top:32px;width:96px;font-style:normal;font-size:6.5px;line-height:1.55;color:var(--ink)}
.lh-footer{position:absolute;left:0;right:0;bottom:0;height:22px;border-top:2px solid var(--blue);
  display:flex;align-items:center;justify-content:center;font-size:6px;color:var(--navy);white-space:nowrap}

/* Business card front */
.card{width:206px;height:146px}
.card-front{left:305px;top:370px;border-right:8px solid var(--blue)}
.card-front .brand{position:absolute;left:12px;top:14px}
.card-front .brand-dot{width:12px;height:12px}
.card-front .brand-name{font-size:9.5px}
.card-front .brand-tag{font-size:6px;margin-top:3px}
.card-details{position:absolute;left:12px;top:66px;font-size:5.5px;line-height:1.6}
.card-doctor{position:absolute;right:10px;top:72px;width:80px;font-size:5.5px;font-weight:600;color:var(--blue);text-transform:uppercase;line-height:1.4}
.card-doctor span{display:block;color:var(--navy);font-weight:400;text-transform:none}

/* Appointment card */
.card-appointment{left:305px;top:533px;height:163px;border-bottom:6px solid var(--blue)}
.appt-body{position:absolute;left:14px;top:14px;width:120px;font-size:6px;line-height:1.5}
.appt-title{font-weight:600;color:var(--navy);font-size:7px;margin-bottom:8px}
.appt-line{display:flex;gap:6px;margin-bottom:9px}
.appt-line i{flex:1;border-bottom:1px solid var(--rule)}
.appt-note{font-size:5px;margin-top:4px}
.card-appointment .brand{position:absolute;right:12px;top:14px}
.card-appointment .brand-name{font-size:8px}
.card-appointment .brand-dot{width:10px;height:10px}

/* Envelopes */
.envelope-back{left:620px;top:220px;width:443px;height:464px;overflow:hidden}
.envelope-back svg{position:absolute;left:0;top:0}
.envelope-front{left:620px;top:475px;width:443px;height:257px}
.envelope-front .brand{position:absolute;left:26px;top:56px}
.envelope-front .brand-dot{width:20px;height:20px}
.envelope-front .brand-name{font-size:17px}
.envelope-front .brand-tag{font-size:9px;margin-top:4px}
.env-footer{position:absolute;left:0;right:0;bottom:0;height:16px;background:var(--blue);color:#fff;
  font-size:5.5px;display:flex;align-items:center;padding-left:12px;letter-spacing:.2px;white-space:nowrap}
</style>
</head>
<body>

<section class="sheet letterhead">
  <div class="brand">
    <div class="brand-dot"></div>
    <div>
      <div class="brand-name">Harbourlea Dental Clinic</div>
      <div class="brand-tag">General &amp; Cosmetic Dentistry</div>
    </div>
  </div>
  <address class="lh-address">Corrow Arcade - Shop 4.3C<br>27 Fenwick Lane<br>Meadowbank, NSW 2114</address>
  <footer class="lh-footer">Phone: 02 5173 6648 &nbsp;|&nbsp; Mobile: 04 7825 1943 &nbsp;|&nbsp; kelsi@HarbourleaDentalClinic.com.au &nbsp;|&nbsp; www.HarbourleaDentalClinic.com.au</footer>
</section>

<section class="sheet card card-front">
  <div class="brand">
    <div class="brand-dot"></div>
    <div>
      <div class="brand-name">Harbourlea Dental Clinic</div>
      <div class="brand-tag">General &amp; Cosmetic Dentistry</div>
    </div>
  </div>
  <div class="card-details">
    Corrow Arcade - Shop 4.3C<br>27 Fenwick Lane<br>Meadowbank, NSW 2114<br>
    After-hours Emergency Service:<br>Phone: 02 5173 6648<br>Mobile: 04 7825 1943<br>
    www.HarbourleaDentalClinic.com.au
  </div>
  <div class="card-doctor">Dr. Kelsi Tomberg Ravinder<span>Dental Surgeon</span></div>
</section>

<section class="sheet card card-appointment">
  <div class="appt-body">
    <div class="appt-title">Appointment:</div>
    <div class="appt-line">For <i></i></div>
    <div class="appt-line">Date <i></i></div>
    <div class="appt-line">Time <i></i></div>
    <p class="appt-note">If you are unable to keep your appointment, please contact us as soon as possible.</p>
  </div>
  <div class="brand">
    <div class="brand-dot"></div>
    <div class="brand-name">Harbourlea</div>
  </div>
</section>

<section class="sheet envelope-back">
  <svg width="443" height="464" viewBox="0 0 443 464">
    <path d="M0 0H443V62C380 104 300 118 221 118S62 104 0 62Z" fill="var(--blue)"/>
    <path d="M0 62C62 104 142 118 221 118S380 104 443 62" fill="none" stroke="#d4e9f5" stroke-width="2"/>
  </svg>
</section>

<section class="sheet envelope-front">
  <div class="brand">
    <div class="brand-dot"></div>
    <div>
      <div class="brand-name">Harbourlea Dental Clinic</div>
      <div class="brand-tag">General &amp; Cosmetic Dentistry</div>
    </div>
  </div>
  <footer class="env-footer">IF NOT DELIVERED PLEASE RETURN TO Corrow Arcade - Shop 4.3C, 27 Fenwick Lane, Meadowbank, NSW 2114</footer>
</section>

</body>
</html>
```